7K Ventures business cards for a tech VC

We're starting a new Venture Capital that is focusing on bringing the best start ups from Israel to NYC
We need a business cards template for this that gives the sense of an entrepreneurial look
I don't want any religious signs on this even thought it's Israel
I'm looking for a techi feeling but not too crazy
The card should probably be in the same light blue as the logo and the logo in white

Target Market(s)

Investors

Industry/Entity Type

Tech

Contact Information for Business Card

The card needs to look slick and entrepreneurship like
The VC is focused on NYC and Tel Aviv so could be great to show something on the back side that is like NYC skyline or something like that
You can see the logo attached

Colors
0455a3
3276b5
85acd3
cedeed
eaf1f7

Requirements
Must have
• A very cool looking business card that shows we're a cutting edge tech VC with a focus on bringing start ups from Tel Aviv and leveraging the NYC ecosystem
Nice to have
• NYC skyline can be cool , maybe something that is connected to Tel Aviv

```html
<!DOCTYPE html>
<html lang="en">
<head>
<meta charset="utf-8">
<title>7K Ventures – Business Card</title>
<link rel="stylesheet" href="https://fonts.googleapis.com/css2?family=Lato:wght@400;700;900&display=swap">
<style>
  :root {
    --deep-blue: #0455a3;
    --mid-blue: #3276b5;
    --soft-blue: #85acd3;
    --pale-blue: #cedeed;
    --mist: #eaf1f7;
    --ink: #1a5a9a;
    --stage: #d9d6d0;
  }
  * { box-sizing: border-box; margin: 0; padding: 0; }
  html, body { width: 1200px; height: 970px; overflow: hidden; }
  body {
    background: var(--stage);
    font-family: "Lato", sans-serif;
    position: relative;
  }
  .card {
    position: absolute;
    left: 80px; top: 190px;
    width: 1040px; height: 590px;
    overflow: hidden;
    background: linear-gradient(160deg, var(--mist) 0%, #f4f7fa 35%, var(--pale-blue) 70%, #e9dcd8 100%);
    box-shadow: 0 10px 30px rgba(0,0,0,0.18);
  }
  .holder { position: absolute; left: 50px; top: 52px; color: var(--ink); }
  .holder-name { font-size: 35px; font-weight: 900; line-height: 1; letter-spacing: 0.2px; }
  .holder-title { font-size: 27px; font-weight: 400; line-height: 1.1; color: var(--mid-blue); }
  .contacts { position: absolute; left: 50px; top: 170px; list-style: none; }
  .contact { display: flex; align-items: center; height: 38px; font-size: 27px; color: var(--ink); }
  .contact-icon { width: 30px; height: 30px; margin-right: 12px; flex: none; }
  .brand {
    position: absolute; right: 48px; top: 120px;
    display: flex; align-items: center; gap: 18px;
    font-size: 62px; font-weight: 900; color: var(--deep-blue);
    line-height: 1;
  }
  .brand-mark { width: 40px; height: 40px; background: var(--deep-blue); }
  .skyline {
    position: absolute; left: 0; bottom: 0;
    width: 100%; height: 330px;
    background: linear-gradient(180deg, rgba(50,118,181,0) 0%, rgba(50,118,181,0.35) 35%, rgba(4,85,163,0.85) 70%, var(--mid-blue) 100%);
  }
  .address {
    position: absolute; left: 0; right: 0; bottom: 16px;
    text-align: center; font-size: 26px; color: var(--pale-blue);
  }
</style>
</head>
<body>
  <section class="card">
    <div class="skyline" role="img" aria-label="New York City skyline silhouette with the Statue of Liberty"></div>

    <div class="holder">
      <div class="holder-name">DANIEL REYES</div>
      <div class="holder-title">Managing Partner</div>
    </div>

    <ul class="contacts">
      <li class="contact">
        <svg class="contact-icon" viewBox="0 0 30 30"><rect width="30" height="30" fill="var(--mid-blue)"/><path d="M7 12c0-3 4-5 8-5s8 2 8 5v2h-4v-2h-8v2H7z M9 15h12l1 8H8z" fill="#fff"/><circle cx="15" cy="19" r="2" fill="var(--mid-blue)"/></svg>
        (02) 4817 3390
      </li>
      <li class="contact">
        <svg class="contact-icon" viewBox="0 0 30 30"><rect width="30" height="30" fill="var(--mid-blue)"/><rect x="6" y="9" width="18" height="12" fill="none" stroke="#fff" stroke-width="1.8"/><path d="M6 9l9 7 9-7M6 21l7-6M24 21l-7-6" fill="none" stroke="#fff" stroke-width="1.6"/></svg>
        Info@7kventures.com
      </li>
      <li class="contact">
        <svg class="contact-icon" viewBox="0 0 30 30"><rect width="30" height="30" fill="var(--mid-blue)"/><g fill="none" stroke="#fff" stroke-width="1.5"><circle cx="15" cy="15" r="8"/><ellipse cx="15" cy="15" rx="3.5" ry="8"/><path d="M7 15h16M8.5 11h13M8.5 19h13"/></g></svg>
        www.7kventures.com
      </li>
    </ul>

    <div class="brand">
      <span class="brand-mark"></span>
      <span class="brand-name">7K Ventures</span>
    </div>

    <p class="address">PO BOX 456 Harbor Lane, 5th Avenue New York, USA</p>
  </section>
</body>
</html>
```